Business cards for Tile Contractor
Brisk Grout Studio
LAST MINUTE ADDITION TO BUSINESS CARD!!
website address: briskgroutstudio.net
and a space after the area code in phone number:
thanks!!
#85 is closest to what im looking for. Thanks for all the drafts! good stuff!
looks good so far. would like to see more with all the info on the card.

```html
<!DOCTYPE html>
<html lang="en">
<head>
<meta charset="utf-8">
<title>Brisk Grout Studio – Stationery</title>
<link rel="stylesheet" href="https://fonts.googleapis.com/css2?family=Roboto:wght@400;700&display=swap">
<style>
  :root {
    --backdrop: #e9e6e1;
    --paper: #ffffff;
    --ink: #2b3440;
    --ink-soft: #6c7682;
    --brand: #1a6fc2;
    --brand-deep: #0b2f66;
    --brand-night: #061a3d;
    --brand-glow: #2f8fe0;
    --envelope-black: #121418;
    --faint: #e4ebf3;
    --shadow: rgba(0, 0, 0, 0.28);
  }
  * { box-sizing: border-box; margin: 0; padding: 0; }
  html, body { width: 1200px; height: 497px; overflow: hidden; }
  body {
    background: var(--backdrop);
    font-family: "Roboto", Arial, sans-serif;
    color: var(--ink);
    position: relative;
  }
  .piece {
    position: absolute;
    background: var(--paper);
    box-shadow: 0 3px 8px var(--shadow);
    overflow: hidden;
  }
  .wordmark {
    display: flex;
    align-items: center;
    gap: 5px;
    font-weight: 700;
    color: var(--brand);
    white-space: nowrap;
    letter-spacing: 0.02em;
  }
  .wordmark .dot {
    border-radius: 50%;
    background: var(--brand);
    flex: none;
  }
  .wordmark.on-dark { color: #ffffff; }
  .wordmark.on-dark .dot { background: #ffffff; }

  /* Business cards */
  .card { width: 175px; height: 97px; border-radius: 6px; }
  .card .wordmark { font-size: 11px; }
  .card .wordmark .dot { width: 14px; height: 14px; }
  .card-tagline {
    position: absolute; left: 0; right: 0; bottom: 12px;
    text-align: center; font-size: 4.6px; line-height: 1.35; color: var(--ink-soft);
  }
  .card-handle {
    position: absolute; right: 8px; bottom: 4px; font-size: 4px; color: var(--ink-soft);
  }
  .card-front { left: 95px; top: 70px; }
  .card-front .face-light {
    position: absolute; top: 0; left: 0; bottom: 0; width: 100px;
    display: flex; align-items: center; padding-left: 8px;
  }
  .card-front .face-light .wordmark { font-size: 7.5px; gap: 4px; letter-spacing: 0; }
  .card-front .face-light .wordmark .dot { width: 10px; height: 10px; }
  .card-front .face-dark {
    position: absolute; top: 0; right: 0; bottom: 0; width: 72px;
    background: radial-gradient(ellipse at 30% 50%, var(--brand-glow), var(--brand-deep) 60%, var(--brand-night));
    border-top-left-radius: 40px 48px; border-bottom-left-radius: 40px 48px;
    color: #ffffff; padding: 12px 4px 0 16px;
  }
  .card-front .person { font-size: 6px; font-weight: 700; }
  .card-front .role { font-size: 4.5px; opacity: 0.85; margin-top: 1px; }
  .card-front .contact { font-size: 4px; line-height: 1.5; margin-top: 14px; opacity: 0.9; white-space: nowrap; }

  .card-back .wordmark { position: absolute; left: 0; right: 0; top: 24px; justify-content: center; }
  .card-back.dark {
    background: radial-gradient(ellipse at 50% 40%, var(--brand-glow), var(--brand-deep) 55%, var(--brand-night));
  }
  .card-back.dark .card-tagline, .card-back.dark .card-handle { color: #cfe0f5; }
  .card-a { left: 12px; top: 188px; }
  .card-b { left: 200px; top: 188px; }
  .card-c { left: 12px; top: 300px; }
  .card-d { left: 200px; top: 300px; }

  /* Letterhead */
  .letterhead { left: 405px; top: 22px; width: 245px; height: 418px; }
  .letterhead .wordmark { position: absolute; left: 20px; top: 20px; font-size: 13px; }
  .letterhead .wordmark .dot { width: 18px; height: 18px; }
  .letterhead .sender {
    position: absolute; right: 14px; top: 18px; font-size: 4.5px; line-height: 1.55; color: var(--ink-soft);
  }
  .letterhead .rule {
    position: absolute; left: 20px; right: 14px; top: 48px; height: 1px; background: var(--faint);
  }
  .faint-disc {
    position: absolute; border-radius: 50%; background: var(--faint);
  }
  .letterhead .faint-disc { width: 110px; height: 110px; left: 68px; top: 150px; }
  .letterhead .footer-swoosh { position: absolute; left: 0; bottom: 0; width: 100%; height: 60px; }

  /* Envelopes */
  .envelope { width: 400px; }
  .envelope-black { left: 790px; top: 20px; height: 110px; background: var(--envelope-black); }
  .envelope-black .flap { position: absolute; inset: 0; }
  .envelope-black .faint-disc {
    width: 34px; height: 34px; left: 183px; top: 42px; background: #ffffff; opacity: 0.9;
  }
  .envelope-white { left: 790px; top: 128px; height: 122px; }
  .envelope-white .flap { position: absolute; inset: 0; }

  .envelope-blue { left: 665px; top: 208px; width: 335px; height: 237px; }
  .envelope-blue .flap { position: absolute; left: 0; top: 0; width: 100%; height: 120px; }
  .envelope-blue .wordmark { position: absolute; left: 22px; top: 110px; font-size: 14px; }
  .envelope-blue .wordmark .dot { width: 20px; height: 20px; }
  .envelope-blue .return-address {
    position: absolute; left: 24px; top: 150px; font-size: 5px; line-height: 1.6; color: var(--ink-soft);
  }
  .envelope-blue .faint-disc { width: 90px; height: 90px; right: 40px; top: 140px; }
</style>
</head>
<body>

  <section class="piece card card-front" aria-label="Business card front">
    <div class="face-light">
      <div class="wordmark"><span class="dot"></span>Brisk Grout Studio</div>
    </div>
    <div class="face-dark">
      <p class="person">Dana Whitfield</p>
      <p class="role">Owner / Installer</p>
      <p class="contact">555 201 4488<br>dana@briskgroutstudio.net<br>briskgroutstudio.net</p>
    </div>
  </section>

  <section class="piece card card-back card-a" aria-label="Business card back">
    <div class="wordmark"><span class="dot"></span>Brisk Grout Studio</div>
    <p class="card-tagline">"Quality tile work at a fair price"<br>Residential &amp; commercial - Free estimates</p>
    <span class="card-handle">Zandu7</span>
  </section>
  <section class="piece card card-back card-b" aria-label="Business card back">
    <div class="wordmark"><span class="dot"></span>Brisk Grout Studio</div>
    <p class="card-tagline">"Quality tile work at a fair price"<br>Residential &amp; commercial - Free estimates</p>
    <span class="card-handle">Zandu7</span>
  </section>
  <section class="piece card card-back card-c" aria-label="Business card back">
    <div class="wordmark"><span class="dot"></span>Brisk Grout Studio</div>
    <p class="card-tagline">"Quality tile work at a fair price"<br>Residential &amp; commercial - Free estimates</p>
    <span class="card-handle">Zandu7</span>
  </section>
  <section class="piece card card-back card-d dark" aria-label="Business card back, dark">
    <div class="wordmark on-dark"><span class="dot"></span>Brisk Grout Studio</div>
    <p class="card-tagline">"Quality tile work at a fair price"<br>Residential &amp; commercial - Free estimates</p>
    <span class="card-handle">Zandu7</span>
  </section>

  <section class="piece letterhead" aria-label="Letterhead">
    <div class="wordmark"><span class="dot"></span>Brisk Grout Studio</div>
    <p class="sender">128 Harbor Lane<br>Westfield, CA 90412<br>Phone: 555 201 4488<br>briskgroutstudio.net</p>
    <div class="rule"></div>
    <div class="faint-disc"></div>
    <svg class="footer-swoosh" viewBox="0 0 245 60" preserveAspectRatio="none" aria-hidden="true">
      <defs>
        <linearGradient id="lh-swoosh" x1="0" x2="1">
          <stop offset="0" stop-color="var(--brand-deep)"/>
          <stop offset="1" stop-color="var(--brand-glow)"/>
        </linearGradient>
      </defs>
      <path d="M0 52 Q120 30 245 44 L245 60 L0 60 Z" fill="url(#lh-swoosh)"/>
      <path d="M0 48 Q120 26 245 40" stroke="var(--brand)" stroke-width="1" fill="none"/>
    </svg>
  </section>

  <section class="piece envelope envelope-black" aria-label="Envelope back, black">
    <svg class="flap" viewBox="0 0 400 110" preserveAspectRatio="none" aria-hidden="true">
      <path d="M0 0 L200 95 L400 0" stroke="#2a2e35" stroke-width="1.5" fill="none"/>
    </svg>
    <div class="faint-disc"></div>
  </section>

  <section class="piece envelope envelope-white" aria-label="Envelope back, white">
    <svg class="flap" viewBox="0 0 400 122" preserveAspectRatio="none" aria-hidden="true">
      <path d="M0 0 L200 70 L400 0" stroke="#d9dde2" stroke-width="1.2" fill="none"/>
      <path d="M0 122 L170 60 M400 122 L230 60" stroke="#e6e9ed" stroke-width="1" fill="none"/>
    </svg>
  </section>

  <section class="piece envelope envelope-blue" aria-label="Envelope front">
    <svg class="flap" viewBox="0 0 335 120" preserveAspectRatio="none" aria-hidden="true">
      <defs>
        <radialGradient id="env-flap" cx="0.5" cy="0.2" r="0.8">
          <stop offset="0" stop-color="var(--brand-glow)"/>
          <stop offset="0.6" stop-color="var(--brand-deep)"/>
          <stop offset="1" stop-color="var(--brand-night)"/>
        </radialGradient>
      </defs>
      <path d="M0 0 L335 0 L335 40 Q167 105 0 40 Z" fill="url(#env-flap)"/>
    </svg>
    <div class="wordmark"><span class="dot"></span>Brisk Grout Studio</div>
    <p class="return-address">128 Harbor Lane<br>Westfield, CA 90412<br>Phone: 555 201 4488<br>Web: briskgroutstudio.net</p>
    <div class="faint-disc"></div>
  </section>

</body>
</html>
```